Brochure - Capabilities Statement doc - 1 page handout

I would like to upgrade our "capabilities statement" brochure doc to look more professional and designed with a tailored modern look. see attached document for details. We use this document when we are in meetings or when we introduce our company in an email to a new prospect client. Its a one page overview of the services we provide. At the moment it is a terrible juvenile looking doc. with no thought to design. I am hoping you can change that and help capture our customers attention when they read it.

Target Market(s)

Our client base is corporations, tech companies and non-profits

Industry/Entity Type

It Professional

Font styles to use
Sans Serif

Requirements
Must have
• I'd like a cleaver sharp look to it. Not just columns and bullet points like I have now. This will be emailed to clients in a pdf and I'd like to have a hand out when in meetings.

```html
<!DOCTYPE html>
<html lang="en">
<head>
<meta charset="utf-8">
<title>Bright Harbor – Capabilities Statement</title>
<link href="https://fonts.googleapis.com/css2?family=Montserrat:wght@400;600;700;800&display=swap" rel="stylesheet">
<style>
  :root {
    --orange: #f0861f;
    --orange-deep: #e57a12;
    --ink: #3a3a3a;
    --ink-soft: #555;
    --white: #ffffff;
    --footer-band: #e9e9e9;
    --label-dark: #4a4a4a;
    --photo-dark: #3b2e2a;
    --photo-mid: #6d5448;
    --photo-warm: #a27b5f;
    --photo-light: #c9b3a0;
  }
  * { margin: 0; padding: 0; box-sizing: border-box; }
  html, body { width: 927px; height: 1200px; overflow: hidden; background: var(--white); }
  body { font-family: "Montserrat", sans-serif; color: var(--ink); }

  .sheet {
    position: relative;
    width: 612px; height: 792px;
    transform: scale(1.5147);
    transform-origin: 0 0;
    overflow: hidden;
    background: var(--white);
  }
  .shapes { position: absolute; inset: 0; width: 612px; height: 792px; }

  .brand-name {
    position: absolute; left: 22px; top: 38px;
    font-size: 20.5px; font-weight: 700; line-height: 1.33;
    letter-spacing: 0.6px; color: var(--ink);
  }
  .intro {
    position: absolute; left: 22px; top: 118px; width: 330px;
    color: var(--white); font-size: 8.6px; line-height: 1.32;
  }
  .intro p + p { margin-top: 11px; }

  .section-title {
    position: absolute;
    color: var(--orange); font-weight: 800; font-size: 11.5px; letter-spacing: 0.2px;
  }
  .check-list {
    position: absolute; list-style: none;
    font-size: 8.4px; line-height: 1.25; color: var(--ink-soft);
  }
  .check-list li { position: relative; padding-left: 17px; }
  .check-list li::before {
    content: ""; position: absolute; left: 0; top: 1px;
    width: 8px; height: 8px; border: 1px solid var(--ink-soft);
  }
  .check-list li::after {
    content: ""; position: absolute; left: 3px; top: -1px;
    width: 3px; height: 7px;
    border-right: 1.4px solid var(--orange-deep); border-bottom: 1.4px solid var(--orange-deep);
    transform: rotate(40deg);
  }
  .capabilities li { margin-bottom: 5.3px; }
  .highlights li { margin-bottom: 3.3px; }
  .difference li { margin-bottom: 7.5px; }
  .partners li { margin-bottom: 4.9px; }

  .codes {
    position: absolute; font-size: 8.6px; color: var(--ink-soft);
  }
  .codes .sep { margin: 0 7px; }

  .cert-label {
    position: absolute; left: 20px; top: 722px;
    color: var(--white); font-size: 8.6px; font-weight: 700; letter-spacing: 0.2px;
  }
  .contact {
    position: absolute; left: 0; width: 612px; text-align: center;
    font-size: 8.6px; color: var(--ink-soft);
  }
  .contact strong { font-weight: 700; color: var(--ink); }
  .contact .sep { margin: 0 9px; }
</style>
</head>
<body>
<div class="sheet">
  <svg class="shapes" viewBox="0 0 612 792" xmlns="http://www.w3.org/2000/svg">
    <!-- header event photography -->
    <g role="img" aria-label="Photo of a conference audience watching a speaker, with inset photos of guests networking and a banquet hall">
      <polygon points="228,0 612,0 612,250 470,318 380,232 300,290 246,230 330,108 248,22" fill="var(--photo-dark)"/>
      <polygon points="430,0 612,0 612,140 500,120" fill="var(--photo-mid)" opacity="0.55"/>
      <polygon points="395,130 450,190 395,250 340,190" fill="var(--photo-warm)" stroke="#fff" stroke-width="2"/>
      <polygon points="470,110 540,185 470,258 400,185" fill="var(--photo-mid)" stroke="#fff" stroke-width="2"/>
      <polygon points="540,120 612,190 612,250 545,260 490,190" fill="var(--photo-light)" stroke="#fff" stroke-width="2"/>
      <polygon points="395,250 440,292 395,330 350,292" fill="var(--photo-light)" stroke="#fff" stroke-width="2"/>
      <polygon points="470,258 515,290 470,320 425,290" fill="var(--photo-warm)" stroke="#fff" stroke-width="2"/>
    </g>
    <!-- white title panel and accents -->
    <polygon points="0,0 238,0 330,108 0,108" fill="var(--white)"/>
    <polygon points="150,0 250,0 228,22" fill="var(--orange)"/>
    <polygon points="0,108 396,108 318,286 0,286" fill="var(--orange)"/>
    <!-- brand circle -->
    <circle cx="372" cy="62" r="40" fill="var(--white)"/>
    <circle cx="372" cy="62" r="35" fill="var(--orange)"/>
    <!-- footer band -->
    <rect x="0" y="710" width="612" height="36" fill="var(--footer-band)"/>
    <polygon points="0,716 220,716 232,729 220,742 0,742" fill="var(--label-dark)"/>
    <!-- certification badges -->
    <circle cx="277" cy="729" r="15" fill="#2c5a9e"/>
    <line x1="308" y1="716" x2="308" y2="742" stroke="#bbb" stroke-width="0.6"/>
    <rect x="344" y="715" width="70" height="28" rx="4" fill="#f3f1e6" stroke="#5e7a3a" stroke-width="1"/>
    <line x1="436" y1="716" x2="436" y2="742" stroke="#bbb" stroke-width="0.6"/>
    <circle cx="471" cy="729" r="14" fill="#c9c4dc"/>
    <line x1="524" y1="716" x2="524" y2="742" stroke="#bbb" stroke-width="0.6"/>
    <circle cx="555" cy="729" r="14" fill="#2a2a2a"/>
  </svg>

  <h1 class="brand-name">BRIGHT<br>HARBOR</h1>

  <div class="intro">
    <p>Bright Harbor is a meeting, event and project management services company. We specialize in capturing your ideas, objectives and budget and transforming them into an unforgettable experience.</p>
    <p>We have been in business for over 18 years and have amassed over 130 years of combined staff experience. With over 38,000 room nights and over 150 events and meetings annually, our ability to leverage our buying power along with our excellent reputation, ensures that our clients procure the best value and service for their investment.</p>
  </div>

  <h2 class="section-title" style="left:20px; top:306px;">CAPABILITIES</h2>
  <ul class="check-list capabilities" style="left:22px; top:331px; width:300px;">
    <li>Site Research and Hotel &amp; Venue Contract Negotiations</li>
    <li>Customized Registration Software &amp; Management</li>
    <li>City-wide Housing Management</li>
    <li>Destination Management Services</li>
    <li>Group Transportation Services</li>
    <li>Airport Meet &amp; Greet Services</li>
    <li>Project Management</li>
    <li>Meeting Management</li>
    <li>Event Management</li>
    <li>Incentive Travel Programs</li>
    <li>Special Event Coordination</li>
    <li>Custom Tours &amp; Activities</li>
    <li>Showroom Installation Services</li>
    <li>Onsite Staff Services / Registration Desk Services &amp; Software</li>
  </ul>

  <h2 class="section-title" style="left:20px; top:573px;">HIGHLIGHTS</h2>
  <ul class="check-list highlights" style="left:22px; top:598px; width:220px;">
    <li>There is no request too large or too small</li>
    <li>Tested and approved suppliers and vendor partnerships</li>
    <li>A-la-carte proposals and services</li>
    <li>Creative experienced team</li>
    <li>We guarantee our work and honor our quotes</li>
  </ul>

  <h2 class="section-title" style="left:354px; top:321px;">WHAT MAKES US DIFFERENT?</h2>
  <ul class="check-list difference" style="left:357px; top:344px; width:230px;">
    <li>Certified Meeting Professionals (CMP)</li>
    <li>Women-Owned Business Certified</li>
    <li>Local, National and International services</li>
    <li>Long-standing client retention through successful partnerships</li>
  </ul>

  <h2 class="section-title" style="left:354px; top:443px;">OUR PARTNERS</h2>
  <ul class="check-list partners" style="left:357px; top:466px; width:230px;">
    <li>Fortune 500 Companies</li>
    <li>Consumer Packaged Goods Industry</li>
    <li>Manufacturing</li>
    <li>Technology Industry</li>
    <li>Non-profit Organizations</li>
    <li>Colleges and Universities</li>
    <li>Client references upon request</li>
  </ul>

  <h2 class="section-title" style="left:354px; top:603px;">NAICS CODES</h2>
  <div class="codes" style="left:354px; top:627px;">561599<span class="sep">|</span>561920</div>

  <h2 class="section-title" style="left:354px; top:653px;">UNSPSC CODES</h2>
  <div class="codes" style="left:354px; top:675px;">80141607</div>

  <div class="cert-label">CERTIFICATIONS AND ASSOCIATIONS</div>

  <p class="contact" style="top:751px;"><strong>BRIGHT HARBOR</strong> PO Box 4820, Lakeview, MI 49990</p>
  <p class="contact" style="top:770px;">Ph. 555.014.2290 x11<span class="sep">|</span>www.brightharborevents.com<span class="sep">|</span>hello@brightharborevents.com</p>
</div>
</body>
</html>
```